Commercial Property Management Company needs business card design

We need an elegant business card design for our commercial property management company based in Hampton Falls, New Hampshire. We manage large retail shopping centers. These cards will be going out to current clients, retailers and to contractors.
I am the sole member of the company, so I'm not sure if I need to have a title with my name or not.

Industry/Entity Type

Property Management

Contact Information for Business Card

Colin R. Mabry
4 Pellow Lane
Alder Ridge, NH 03990
Cell: (603) 555-0142
Fax: (603) 555-0187
Email: colin@tovrenmanagementllc.com

```html
<!DOCTYPE html>
<html lang="en">
<head>
<meta charset="utf-8">
<title>Tovren Management, LLC — Business Card</title>
<link rel="stylesheet" href="https://fonts.googleapis.com/css2?family=Cinzel:wght@500&family=Mulish:wght@400;700&display=swap">
<style>
  :root {
    --backdrop: #c9d0da;
    --card: #f4f4f2;
    --ink: #1f1f1f;
    --ink-soft: #3a3a3a;
    --rule: #9a9a9a;
    --maroon: #6a1d12;
  }
  * { box-sizing: border-box; margin: 0; padding: 0; }
  html, body { width: 1200px; height: 1000px; overflow: hidden; }
  body {
    background: var(--backdrop);
    position: relative;
    font-family: "Mulish", sans-serif;
    color: var(--ink);
  }
  .card {
    position: absolute;
    width: 700px;
    height: 400px;
    background: var(--card);
    box-shadow: 0 10px 30px rgba(40, 50, 70, 0.18);
  }

  /* Front of card */
  .card-front { top: 70px; left: 440px; }
  .front-mark {
    position: absolute;
    top: 70px;
    left: 50%;
    transform: translateX(-50%);
    width: 96px;
    height: 96px;
    border-radius: 50%;
    background: var(--maroon);
  }
  .front-lockup {
    position: absolute;
    top: 190px;
    left: 0;
    right: 0;
    display: flex;
    flex-direction: column;
    align-items: center;
  }
  .company-name {
    font-family: "Cinzel", serif;
    font-weight: 500;
    font-size: 40px;
    letter-spacing: 0.5px;
    color: var(--ink);
    line-height: 1;
  }
  .tagline {
    align-self: flex-end;
    margin-right: 100px;
    margin-top: 6px;
    font-weight: 700;
    font-size: 17px;
    color: var(--ink);
  }

  /* Back of card */
  .card-back { top: 540px; left: 60px; }
  .back-brand {
    position: absolute;
    top: 110px;
    left: 50px;
    width: 200px;
    display: flex;
    flex-direction: column;
    align-items: center;
    gap: 14px;
  }
  .back-mark {
    width: 130px;
    height: 130px;
    border-radius: 50%;
    background: var(--maroon);
  }
  .back-name {
    font-weight: 700;
    font-size: 16px;
    color: var(--maroon);
    white-space: nowrap;
  }
  .contact {
    position: absolute;
    top: 78px;
    left: 300px;
    font-size: 17px;
    line-height: 27px;
    color: var(--ink-soft);
  }
  .contact-name { font-weight: 700; color: var(--ink); }
  .contact-rule { color: var(--rule); line-height: 18px; }
  .contact-label { display: inline-block; width: 26px; }
  .contact-indent { padding-left: 26px; }
</style>
</head>
<body>

  <section class="card card-front" aria-label="Card front">
    <div class="front-mark"></div>
    <div class="front-lockup">
      <div class="company-name">Tovren Management, LLC</div>
      <div class="tagline">Commercial property management</div>
    </div>
  </section>

  <section class="card card-back" aria-label="Card back">
    <div class="back-brand">
      <div class="back-mark"></div>
      <div class="back-name">Tovren Management</div>
    </div>
    <div class="contact">
      <div class="contact-name">Colin R. Mabry</div>
      <div>Tovren Management</div>
      <div class="contact-rule">—</div>
      <div><span class="contact-label">T:</span>(603) 555-0142</div>
      <div><span class="contact-label">F:</span>(603) 555-0187</div>
      <div><span class="contact-label">E:</span>colin@tovrenmanagementllc.com</div>
      <div class="contact-rule">—</div>
      <div><span class="contact-label">A:</span>4 Pellow Lane</div>
      <div class="contact-indent">Alder Ridge, NH 03990</div>
    </div>
  </section>

</body>
</html>
```